Box truck wrap design for my business BrickNest Seal and Slab

A simple, modern design for a box truck. Truck dimensions are as follows.

Sides - 181"W x 84"H
Back Rollup Door - 87 3/4"W x 85 1/4"H

Brand guidelines have been attached along with examples of wraps that I like. Just need to apply this to an valtro box truck. Website is bricknest-crew.example which you can use as inspiration. Slogan is 'Weather Tight, Foundation Right"

Target Market(s)

Insulation, Waterproofing, Foundation Repair

Industry/Entity Type

Construction - Home Services

Font styles to use
Other font styles liked:
• use brand guidelines attached

Colors

Designer to choose colors to be used in the design.

Requirements
Must have
• bricknest-crew.example , 555-214-7739

```html
<!DOCTYPE html>
<html lang="en">
<head>
<meta charset="utf-8">
<title>BrickNest Seal and Slab – Box Truck Side Wrap</title>
<link rel="stylesheet" href="https://fonts.googleapis.com/css2?family=Orbitron:wght@700;800&family=Audiowide&family=Roboto:wght@900&display=swap">
<style>
  :root {
    --stage: #e9ebee;
    --wrap-white: #ffffff;
    --charcoal: #2e3236;
    --charcoal-deep: #25282b;
    --orange: #f0651f;
    --orange-bright: #ff7a2a;
    --sun: #f8bd2c;
    --roof-pink: #ee6fa5;
    --slate: #c9ccd1;
    --text-light: #ffffff;
    --text-dark: #25282b;
  }
  * { margin: 0; padding: 0; box-sizing: border-box; }
  html, body { width: 1200px; height: 799px; overflow: hidden; background: var(--stage); }
  .wrap-side {
    position: absolute; left: 40px; top: 156px;
    width: 1120px; height: 486px;
    background: var(--wrap-white);
    overflow: hidden;
  }
  .wrap-art { position: absolute; inset: 0; width: 100%; height: 100%; }
  .ribbon-label {
    position: absolute; left: 14px; top: 44px;
    font: 900 15px/1 "Roboto", sans-serif; letter-spacing: 0.5px;
    color: var(--text-light); transform: rotate(-28deg); transform-origin: left top;
    white-space: nowrap;
  }
  .web-address {
    position: absolute; right: 48px; top: 18px;
    font: 900 10px/1 "Roboto", sans-serif; color: var(--text-dark);
  }
  .brand {
    position: absolute; left: 365px; width: 357px; top: 92px;
    text-align: center; color: var(--text-light);
  }
  .brand-mark { width: 44px; height: 44px; background: var(--orange); margin: 0 auto 38px; }
  .brand-name { font: 800 34px/1 "Orbitron", sans-serif; letter-spacing: 1px; }
  .brand-sub { font: 700 13px/1 "Orbitron", sans-serif; letter-spacing: 3px; margin-top: 8px; padding-top: 5px; border-top: 2px solid var(--slate); display: inline-block; }
  .slogan {
    position: absolute; left: 405px; width: 277px; top: 272px;
    font: 900 10px/1.35 "Roboto", sans-serif; text-transform: uppercase;
    color: var(--text-light); text-align: center;
  }
  .phone {
    position: absolute; left: 690px; top: 378px;
    font: 700 27px/1 "Orbitron", sans-serif; letter-spacing: 1px; color: var(--text-dark);
  }
  .services {
    position: absolute; left: 0; bottom: 0; width: 100%; height: 43px;
    display: flex; align-items: center; justify-content: space-around;
    list-style: none; padding: 0 30px;
    font: 21px/1 "Audiowide", sans-serif; color: var(--text-light);
  }
</style>
</head>
<body>
  <section class="wrap-side">
    <svg class="wrap-art" viewBox="0 0 1120 486" aria-hidden="false">
      <defs>
        <radialGradient id="warm-home" cx="50%" cy="50%" r="50%">
          <stop offset="0%" stop-color="#f6c4a8"/>
          <stop offset="60%" stop-color="#f2a3c0"/>
          <stop offset="100%" stop-color="var(--sun)"/>
        </radialGradient>
        <linearGradient id="worn-home" x1="0" y1="0" x2="0" y2="1">
          <stop offset="0%" stop-color="#d3d6da"/>
          <stop offset="70%" stop-color="#b9bdc3"/>
          <stop offset="100%" stop-color="#3a3d41"/>
        </linearGradient>
      </defs>
      <polygon class="ribbon" points="0,92 172,0 250,0 0,134" fill="var(--charcoal)"/>
      <path class="illustration-damaged-home" role="img" aria-label="Illustration of a grey house with a cracked wall and repair tools"
            d="M20,400 L20,230 A170,170 0 0 1 360,230 L360,400 Z" fill="url(#worn-home)"/>
      <circle class="illustration-restored-home" role="img" aria-label="Illustration of a bright, repaired pink and yellow house with air-flow arrows on a sunny backdrop"
              cx="895" cy="205" r="165" fill="url(#warm-home)"/>
      <path class="orange-wave" d="M0,408 C280,400 560,352 1120,340 L1120,443 L0,443 Z" fill="var(--orange)"/>
      <polygon class="brand-hexagon" points="543,6 722,103 722,346 548,425 365,346 365,103" fill="var(--charcoal)"/>
      <rect class="service-strip" x="0" y="443" width="1120" height="43" fill="var(--charcoal-deep)"/>
    </svg>

    <div class="ribbon-label">PROTECT YOUR HOME</div>
    <div class="web-address">https://bricknest-crew.example</div>

    <div class="brand">
      <div class="brand-mark"></div>
      <div class="brand-name">BRICKNEST</div>
      <div class="brand-sub">SEAL AND SLAB</div>
    </div>

    <p class="slogan">Weather Tight, Foundation Right<br>Expert foundation, waterproofing,<br>and insulation services</p>

    <div class="phone">CALL: (555) 214-7739</div>

    <ul class="services">
      <li>Insulation</li>
      <li>Waterproofing</li>
      <li>Indoor Air Quality</li>
      <li>Foundation Repair</li>
    </ul>
  </section>
</body>
</html>
```